Pelbrooks Burgers and Tacos needs a new menu board design

We are a fast casual restaurant that sells burgers, tacos, wraps and other items. We have a California feel, sleek and modern, décor has photos of people like Vormack, Tessard, Brastow. Song list varies from Copper Lanterns, Amber Meridian, Corvanes, Halloway Brightmoor etc... Our main goal for this project is to clean up the look of our menu boards...make them easier to read and more reflective of the style of the restaurant. We also want to feature our combos which are our high profit items...think they should take up 30 to 40% of the space.

We have t-shirts that say "Don't Worry Be Hippy", "Carry Me Down Slowly", "Make Tacos Not War".

There is potential for other projects such as outdoor menu panels, paper menus, promotional items. I am attaching a layout of the menu panels as they appear now with dimensions. Also photos of the restaurant. We are not planning to use these same panels so please don't design around them...come up with your own ideas on this....there is a slightly curved background. We have a really good sign person that can customize if need be.

We have had this menu for a long time and it needs to be clean and sleek.

Target Market(s)

teenagers to 40+

Industry/Entity Type

Restaurant

Requirements
Must have
• Clean readable headers

```html
<!DOCTYPE html>
<html lang="en">
<head>
<meta charset="utf-8">
<title>Pelbrooks Burgers and Tacos – Menu Board</title>
<link href="https://fonts.googleapis.com/css2?family=Luckiest+Guy&family=Chewy&family=Oswald:wght@500;700&family=Open+Sans:wght@400;600&display=swap" rel="stylesheet">
<style>
  :root {
    --bg: #000000;
    --frame-grey: #8a8a8a;
    --frame-dark: #141414;
    --frame-yellow: #f6c40f;
    --board: #2a2a2c;
    --magenta: #a62a9c;
    --yellow: #ffd21a;
    --green: #6cc04a;
    --white: #ffffff;
    --tile-1: #111634;
    --tile-2: #1f3d6b;
    --tile-3: #2f6f9e;
  }
  * { box-sizing: border-box; margin: 0; padding: 0; }
  html, body { width: 1200px; height: 960px; overflow: hidden; background: var(--bg); }
  .canvas { position: relative; width: 1200px; height: 960px; background: var(--bg); }

  .combo-heading {
    position: absolute; left: 170px; top: 268px; z-index: 3;
    font-family: "Luckiest Guy", sans-serif; font-size: 44px; line-height: 1; color: var(--yellow);
    -webkit-text-stroke: 2px #111; paint-order: stroke fill;
    text-shadow: 3px 3px 0 #111;
    letter-spacing: 1px;
  }

  .brand {
    position: absolute; left: 420px; top: 214px; z-index: 4;
    font-family: "Oswald", sans-serif; font-weight: 700; color: var(--yellow);
  }
  .brand-name { display: block; font-size: 80px; line-height: 1; letter-spacing: 1px; }
  .brand-dot {
    position: absolute; right: -32px; top: 4px; width: 22px; height: 22px; border-radius: 50%;
    background: var(--green);
  }

  .menu-board {
    position: absolute; left: 60px; top: 320px; width: 1080px; height: 362px;
    border-radius: 48px; background: var(--board);
    border: 9px solid var(--frame-grey);
    box-shadow: inset 0 0 0 5px var(--frame-dark), inset 0 0 0 9px var(--frame-yellow), inset 0 0 0 11px var(--frame-dark);
  }
  .board-inner { position: absolute; inset: 11px; border-radius: 36px; overflow: hidden; }
  .pattern-fill { position: absolute; inset: 0; background: var(--board); }
  .combo-panel { position: absolute; left: 0; top: 0; width: 420px; height: 100%; }

  .brand-sub {
    position: absolute; left: 372px; top: 14px; z-index: 3;
    font-family: "Oswald", sans-serif; font-weight: 700; font-size: 22px; line-height: 1;
    letter-spacing: 4px; color: var(--white);
  }

  .tagline {
    position: absolute; left: 770px; top: 14px; z-index: 3;
    font-family: "Chewy", sans-serif; font-size: 28px; line-height: 1; color: var(--green);
    transform: rotate(5deg);
  }

  .combo-grid {
    position: absolute; left: 18px; top: 10px; z-index: 2;
    display: grid; grid-template-columns: repeat(3, 100px); grid-auto-rows: 96px; gap: 8px;
  }
  .combo-tile {
    position: relative; border-radius: 14px; border: 2px solid var(--white);
    color: var(--white); padding: 4px 6px;
    font-family: "Oswald", sans-serif; font-weight: 700;
  }
  .row-1 { background: linear-gradient(135deg, var(--tile-1), #1b2656); }
  .row-2 { background: linear-gradient(135deg, #1a3463, var(--tile-2) 60%, #255183); }
  .row-3 { background: linear-gradient(135deg, #26588a, var(--tile-3) 60%, #3a84b6); }
  .combo-title { display: flex; align-items: flex-end; }
  .combo-number { font-size: 28px; color: var(--yellow); line-height: 1; margin-right: 3px; }
  .combo-name { font-size: 12px; line-height: 1.3; }
  .combo-item { display: block; font-size: 13px; line-height: 1.2; margin-top: 2px; }
  .combo-price {
    position: absolute; right: 8px; bottom: 4px; color: var(--yellow);
    font-size: 30px; line-height: 1;
  }
  .combo-price sup { font-size: 15px; vertical-align: 12px; margin-left: 2px; }

  .menu-list { position: absolute; top: 100px; z-index: 2; width: 280px; list-style: none; }
  .menu-list.col-left { left: 440px; }
  .menu-list.col-right { left: 740px; }
  .menu-item { height: 42px; }
  .item-name {
    display: block; font-family: "Oswald", sans-serif; font-weight: 700; font-size: 15px; line-height: 1.1;
    color: var(--yellow); text-shadow: 1px 1px 0 #000;
  }
  .item-line {
    display: flex; align-items: baseline; font-family: "Open Sans", sans-serif; font-weight: 600;
    font-size: 10.5px; color: var(--white); line-height: 1.3; white-space: nowrap;
  }
  .item-leader { flex: 1; border-bottom: 1px dotted var(--white); margin: 0 3px; transform: translateY(-3px); }
</style>
</head>
<body>
<div class="canvas">

  <div class="combo-heading">COMBOS</div>

  <div class="brand">
    <span class="brand-name">PELBROOKS</span>
    <span class="brand-dot"></span>
  </div>

  <div class="menu-board">
    <div class="board-inner">
      <div class="pattern-fill" role="img" aria-label="Dark charcoal background with a repeating small peace-symbol pattern"></div>
      <svg class="combo-panel" viewBox="0 0 420 320" preserveAspectRatio="none" role="img" aria-label="Magenta combo panel with a repeating peace-symbol pattern and a curved right edge">
        <path d="M0 0 H345 Q352 170 395 320 H0 Z" fill="var(--magenta)"/>
        <path d="M345 0 Q352 170 395 320" fill="none" stroke="var(--white)" stroke-width="3"/>
      </svg>

      <div class="brand-sub">BURGERS &amp; TACOS</div>
      <div class="tagline">It's "Pelbrook-a-licious!"</div>

      <div class="combo-grid">
        <div class="combo-tile row-1"><div class="combo-title"><span class="combo-number">1</span><span class="combo-name">Pelbrooks</span></div><span class="combo-item">Cheeseburger</span><span class="combo-price">8<sup>69</sup></span></div>
        <div class="combo-tile row-1"><div class="combo-title"><span class="combo-number">2</span><span class="combo-name">Pelbrooks</span></div><span class="combo-item">Cheeseburger</span><span class="combo-price">8<sup>69</sup></span></div>
        <div class="combo-tile row-1"><div class="combo-title"><span class="combo-number">3</span><span class="combo-name">Pelbrooks</span></div><span class="combo-item">Cheeseburger</span><span class="combo-price">8<sup>69</sup></span></div>
        <div class="combo-tile row-2"><div class="combo-title"><span class="combo-number">4</span><span class="combo-name">Pelbrooks</span></div><span class="combo-item">Cheeseburger</span><span class="combo-price">8<sup>69</sup></span></div>
        <div class="combo-tile row-2"><div class="combo-title"><span class="combo-number">5</span><span class="combo-name">Pelbrooks</span></div><span class="combo-item">Cheeseburger</span><span class="combo-price">8<sup>69</sup></span></div>
        <div class="combo-tile row-2"><div class="combo-title"><span class="combo-number">6</span><span class="combo-name">Pelbrooks</span></div><span class="combo-item">Cheeseburger</span><span class="combo-price">8<sup>69</sup></span></div>
        <div class="combo-tile row-3"><div class="combo-title"><span class="combo-number">7</span><span class="combo-name">Pelbrooks</span></div><span class="combo-item">Cheeseburger</span><span class="combo-price">8<sup>69</sup></span></div>
        <div class="combo-tile row-3"><div class="combo-title"><span class="combo-number">8</span><span class="combo-name">Pelbrooks</span></div><span class="combo-item">Cheeseburger</span><span class="combo-price">8<sup>69</sup></span></div>
        <div class="combo-tile row-3"><div class="combo-title"><span class="combo-number">9</span><span class="combo-name">Pelbrooks</span></div><span class="combo-item">Cheeseburger</span><span class="combo-price">8<sup>69</sup></span></div>
      </div>

      <ul class="menu-list col-left">
        <li class="menu-item"><span class="item-name">Pelbrooks Cheeseburger</span><span class="item-line">Swiss or cheddar, Choice of lettuce, tomato<span class="item-leader"></span>5.89</span></li>
        <li class="menu-item"><span class="item-name">Pelbrooks Cheeseburger</span><span class="item-line">Swiss or cheddar, Choice of lettuce, tomato<span class="item-leader"></span>5.89</span></li>
        <li class="menu-item"><span class="item-name">Pelbrooks Cheeseburger</span><span class="item-line">Swiss or cheddar, Choice of lettuce, tomato<span class="item-leader"></span>5.89</span></li>
        <li class="menu-item"><span class="item-name">Pelbrooks Cheeseburger</span><span class="item-line">Swiss or cheddar, Choice of lettuce, tomato<span class="item-leader"></span>5.89</span></li>
        <li class="menu-item"><span class="item-name">Pelbrooks Cheeseburger</span><span class="item-line">Swiss or cheddar, Choice of lettuce, tomato<span class="item-leader"></span>5.89</span></li>
      </ul>
      <ul class="menu-list col-right">
        <li class="menu-item"><span class="item-name">Pelbrooks Cheeseburger</span><span class="item-line">Swiss or cheddar, Choice of lettuce, tomato<span class="item-leader"></span>5.89</span></li>
        <li class="menu-item"><span class="item-name">Pelbrooks Cheeseburger</span><span class="item-line">Swiss or cheddar, Choice of lettuce, tomato<span class="item-leader"></span>5.89</span></li>
        <li class="menu-item"><span class="item-name">Pelbrooks Cheeseburger</span><span class="item-line">Swiss or cheddar, Choice of lettuce, tomato<span class="item-leader"></span>5.89</span></li>
        <li class="menu-item"><span class="item-name">Pelbrooks Cheeseburger</span><span class="item-line">Swiss or cheddar, Choice of lettuce, tomato<span class="item-leader"></span>5.89</span></li>
        <li class="menu-item"><span class="item-name">Pelbrooks Cheeseburger</span><span class="item-line">Swiss or cheddar, Choice of lettuce, tomato<span class="item-leader"></span>5.89</span></li>
      </ul>
    </div>
  </div>

</div>
</body>
</html>
```